Website design for dressage horse training business

Looking to develop a new website design for a dressage horse training website. We want to change from a single landing page to one with multiple pages.
You are free to use your creativity to design the main landing page. This is the only page you need to design at this point. I would encourage looking at other Dressage Training websites to get a feel for what is typically on them. A few websites are listed below although I think the design of them could be better.
Notes:
- Menu to include: Home, Services, News Room, Blog, About Us, Contact,
- FAQ section on main page
- Logo to remain the same - the logo attached is not the correct color so change to match existing color.
- Change 'Sponsors' to 'Partnerships' on main page
Here is the link to the current site:
https://lindenridgestables.com/
Example sites
https://www.crestwoodsporthorsesco.com/
https://corinnalavelledressage.com/
Target Market(s)
Older women with disposable income
Number of Pages Required
1 page
Look and feel
Each slider illustrates characteristics of the customer's brand and the style your logo design should communicate.

```html
<!DOCTYPE html>
<html lang="en">
<head>
<meta charset="utf-8">
<title>Linden Ridge – Dressage And Sport Horse Training</title>
<link href="https://fonts.googleapis.com/css2?family=Poppins:wght@400;500;600;700&display=swap" rel="stylesheet">
<style>
:root{
  --ink:#222222;
  --body:#555555;
  --muted:#777777;
  --accent:#c49a6c;
  --white:#ffffff;
  --light:#f3f3f3;
  --dark:#151515;
  --line:#e2e2e2;
  --star:#f29a1f;
}
*{margin:0;padding:0;box-sizing:border-box}
html,body{width:1200px;height:4906px;overflow:hidden}
body{font-family:'Poppins',sans-serif;color:var(--ink);background:var(--white);position:relative}
.abs{position:absolute}
.photo{position:absolute;display:block}
.btn{position:absolute;display:flex;align-items:center;justify-content:center;border-radius:26px;font-size:12px;font-weight:600}
.btn-outline{border:1px solid #999;color:var(--ink);background:var(--white)}
.btn-accent{background:var(--accent);color:var(--white);box-shadow:0 8px 18px rgba(196,154,108,.35)}
.eyebrow{position:absolute;left:0;width:1200px;text-align:center;font-size:16px;color:var(--ink)}
.section-title{position:absolute;left:0;width:1200px;text-align:center;font-size:28px;font-weight:600;color:var(--ink);line-height:1.35}

/* header / hero */
.hero{position:absolute;left:0;top:0;width:1200px;height:606px;background:linear-gradient(180deg,#2f4a1f 0%,#3f5e27 40%,#56753a 62%,#6f8f8e 80%,#b9bec6 100%)}
.hero-banner{position:absolute;left:0;top:470px;width:1200px;height:136px;background:linear-gradient(90deg,#5f9aa0 0%,#a9c8c4 30%,#c7c9cf 60%,#d8d9dc 100%)}
.hero-feature{position:absolute;left:596px;top:70px;width:420px;height:536px;border-radius:210px 210px 0 0;background:linear-gradient(170deg,#3b2a22 0%,#5a3420 45%,#3a2216 100%)}
.logo{position:absolute;left:185px;top:16px;font-size:26px;font-weight:600;color:var(--white);letter-spacing:1px}
.nav{position:absolute;left:440px;top:22px;display:flex;gap:26px;font-size:13px;color:var(--white)}
.login{position:absolute;left:941px;top:15px;width:75px;height:33px;border-radius:17px;background:var(--white);color:var(--ink);font-size:12px;font-weight:600;display:flex;align-items:center;justify-content:center}
.hero-kicker{position:absolute;left:183px;top:164px;font-size:14px;color:var(--white)}
.hero-title{position:absolute;left:183px;top:205px;font-size:40px;font-weight:700;line-height:1.22;color:var(--white)}
.hero-text{position:absolute;left:183px;top:336px;width:330px;font-size:14px;line-height:1.6;color:var(--white)}

/* about */
.about-text{position:absolute;left:634px;top:804px;width:366px;font-size:14px;line-height:24px;color:var(--body)}

/* services */
.services{position:absolute;left:0;top:1238px;width:1200px;height:667px;background:linear-gradient(180deg,#f6f6f4 0%,#eeeeea 55%,#f3f2ee 100%)}
.card-title{position:absolute;font-size:20px;font-weight:600;color:var(--ink)}
.card-text{position:absolute;width:205px;font-size:12px;line-height:20px;color:var(--body)}

/* video */
.arrow{position:absolute;width:36px;height:36px;border-radius:50%;background:rgba(255,255,255,.85);display:flex;align-items:center;justify-content:center}

/* faq */
.faq-item{position:absolute;left:611px;width:404px;border-bottom:1px solid var(--line)}
.faq-q{font-size:19px;font-weight:500;line-height:30px;color:var(--ink);width:300px}
.faq-a{font-size:11px;line-height:19px;color:var(--muted);margin-top:10px;width:360px}
.faq-icon{position:absolute;right:8px;top:0;font-size:20px;color:#999}

/* testimonials */
.avatar{position:absolute;width:52px;height:52px;border-radius:50%;background:linear-gradient(135deg,#6b5a45,#2f4d2a)}
.t-name{position:absolute;font-size:19px;font-weight:500;color:var(--ink)}
.t-role{position:absolute;font-size:14px;color:var(--muted)}
.t-text{position:absolute;width:245px;font-size:14px;line-height:22px;color:var(--body)}
.stars{position:absolute;font-size:11px;letter-spacing:1px;color:var(--star)}
.dot{position:absolute;width:6px;height:6px;border-radius:50%;background:#bbb}

/* partnerships */
.partners{position:absolute;left:0;top:3783px;width:1200px;height:564px;background:radial-gradient(ellipse at 50% 30%,#2a2a26 0%,#161614 60%,#0f0f0e 100%)}
.p-mark{position:absolute;display:flex;align-items:center;gap:10px;font-size:15px;font-weight:600;color:var(--white)}
.p-mark span.shape{width:34px;height:34px;border-radius:50%;background:#8c2a1e}
.p-name{position:absolute;font-size:23px;font-weight:600;color:var(--white)}
.p-text{position:absolute;width:300px;font-size:14px;line-height:22px;color:#dddddd}
.btn-ghost{border:1px solid #bbb;color:var(--white);background:transparent}

/* footer */
.footer{position:absolute;left:0;top:4347px;width:1200px;height:559px;background:var(--light)}
.cta-title{position:absolute;left:183px;top:4422px;font-size:24px;font-weight:600;line-height:1.4;color:var(--ink)}
.f-head{position:absolute;font-size:14px;font-weight:600;color:var(--ink)}
.f-list{position:absolute;list-style:none;font-size:11px;line-height:26px;color:var(--ink)}
.f-text{position:absolute;font-size:11px;line-height:19px;color:var(--ink)}
.social{position:absolute;width:12px;height:12px;border-radius:50%;background:var(--ink)}
.copyright{position:absolute;left:0;top:4779px;width:1200px;text-align:center;font-size:11px;color:var(--ink)}
</style>
</head>
<body>

<!-- Header and hero -->
<section class="hero" role="img" aria-label="Show jumping arena with trees behind and sponsor banners along the fence">
  <div class="hero-banner"></div>
</section>
<div class="hero-feature" role="img" aria-label="Rider on a bay horse jumping a fence"></div>
<div class="logo">Linden Ridge</div>
<nav class="nav"><span>Home</span><span>Services</span><span>News Room</span><span>Blog</span><span>About Us</span><span>Contact</span></nav>
<div class="login">Login</div>
<p class="hero-kicker">Welcome To</p>
<h1 class="hero-title">Dressage And Sport<br>Horse Training.</h1>
<p class="hero-text">Lorem ipsum dolor sit amet consectetur adipisicing elit seddo eiusm.</p>
<div class="btn btn-outline" style="left:183px;top:419px;width:131px;height:50px;border:none">Our Services</div>

<!-- About -->
<div class="photo" style="left:185px;top:701px;width:404px;height:450px;background:linear-gradient(160deg,#8a6a4a 0%,#3a2a1e 45%,#6d6458 100%)" role="img" aria-label="Young rider in a helmet standing beside her saddled horse"></div>
<p class="abs" style="left:634px;top:697px;font-size:16px">About us</p>
<h2 class="abs" style="left:634px;top:745px;font-size:27px;font-weight:600">What Is Dressage?</h2>
<p class="about-text">Grand Prix rider and trainer, Clara Whitcombe began her riding career at a young age. She went up through the ranks of Junior Riders Guild and with an emphasis and focus in eventing. During college, Clara worked for a small breeder starting young horses. Clara loves starting young horses including starting and guiding them in a correct and quiet way to help them flourish. Her training focuses on gymnastic training incorporating ground.</p>
<div class="btn btn-outline" style="left:634px;top:1080px;width:130px;height:50px">Our Services</div>

<!-- Services -->
<section class="services"></section>
<p class="eyebrow" style="top:1304px">Our Service</p>
<h2 class="section-title" style="top:1344px">Training &amp; Lessons</h2>
<div class="photo" style="left:185px;top:1438px;width:261px;height:280px;background:linear-gradient(180deg,#bcd3e4 0%,#4f6d3a 55%,#8a6a48 100%)" role="img" aria-label="Two riders on horseback in an outdoor arena"></div>
<div class="photo" style="left:470px;top:1438px;width:261px;height:280px;background:linear-gradient(180deg,#9aa0a2 0%,#5a3e2c 50%,#2c2420 100%)" role="img" aria-label="Rider greeting a horse in a stable aisle"></div>
<div class="photo" style="left:754px;top:1438px;width:261px;height:280px;background:linear-gradient(180deg,#c9d2d6 0%,#7a7e6c 45%,#3e3228 100%)" role="img" aria-label="Two horses standing by a fence in front of a mountain"></div>
<h3 class="card-title" style="left:205px;top:1731px">Training</h3>
<h3 class="card-title" style="left:490px;top:1731px">Lessons</h3>
<h3 class="card-title" style="left:775px;top:1731px">Sale Horses</h3>
<p class="card-text" style="left:205px;top:1777px">Lorem ipsum dolor sit amet con sectetur adipisicing elit.</p>
<p class="card-text" style="left:490px;top:1777px">Lorem ipsum dolor sit amet con sectetur adipisicing elit.</p>
<p class="card-text" style="left:775px;top:1777px">Lorem ipsum dolor sit amet con sectetur adipisicing.</p>

<!-- Video -->
<p class="eyebrow" style="top:1977px">Explore Video</p>
<h2 class="section-title" style="top:2022px">Want To Improve Your<br>Dressage Seat?</h2>
<div class="photo" style="left:0;top:2156px;width:272px;height:324px;background:linear-gradient(180deg,#9a9a9a 0%,#5e5e5e 55%,#b5b5b5 100%)" role="img" aria-label="Black and white photo of a rider cantering in an arena"></div>
<div class="photo" style="left:954px;top:2156px;width:246px;height:324px;background:linear-gradient(180deg,#a8a8a8 0%,#505050 55%,#9c9c9c 100%)" role="img" aria-label="Black and white photo of horses galloping on a track"></div>
<div class="photo" style="left:272px;top:2156px;width:682px;height:353px;background:linear-gradient(180deg,#b7c6cf 0%,#6c8a5a 40%,#d8d6d0 62%,#8a7a64 100%);box-shadow:0 12px 24px rgba(0,0,0,.2)" role="img" aria-label="Video still of two riders on horseback at a racecourse"></div>
<div class="arrow" style="left:254px;top:2314px"><svg width="10" height="14" viewBox="0 0 10 14"><path d="M7 2 2 7l5 5" fill="none" stroke="#333" stroke-width="1.6"/></svg></div>
<div class="arrow" style="left:936px;top:2314px"><svg width="10" height="14" viewBox="0 0 10 14"><path d="M3 2l5 5-5 5" fill="none" stroke="#333" stroke-width="1.6"/></svg></div>
<div class="arrow" style="left:591px;top:2309px;width:46px;height:46px"><svg width="14" height="16" viewBox="0 0 14 16"><path d="M2 1l11 7-11 7z" fill="#c49a6c"/></svg></div>

<!-- FAQ -->
<p class="eyebrow" style="top:2581px">FAQ</p>
<h2 class="section-title" style="top:2621px">How can We Help You?</h2>
<div class="photo" style="left:185px;top:2711px;width:392px;height:497px;background:linear-gradient(180deg,#d8dde2 0%,#8a8a5a 35%,#4e6a2e 70%,#6a8a3e 100%)" role="img" aria-label="Rider on a bay horse jumping a pole fence in a grass field"></div>
<div class="faq-item" style="top:2705px;height:84px"><p class="faq-q">How and where can I find work experience?</p><span class="faq-icon">+</span></div>
<div class="faq-item" style="top:2808px;height:110px"><p class="faq-q">Does it matter that I cannot ride?</p><p class="faq-a">Lorem ipsum dolor sit amet, consectetur adipisicing elit, sed do eiusmod tempor incididunt.</p><span class="faq-icon">–</span></div>
<div class="faq-item" style="top:2945px;height:84px"><p class="faq-q">What weight and height do I need to be?</p><span class="faq-icon">+</span></div>
<div class="faq-item" style="top:3056px;height:84px;border-bottom:none"><p class="faq-q">What opportunities are there to advance my career?</p><span class="faq-icon">+</span></div>
<div class="btn btn-accent" style="left:611px;top:3158px;width:130px;height:50px">View All FAQ</div>

<!-- Testimonials -->
<p class="eyebrow" style="top:3291px">Testimonials</p>
<h2 class="section-title" style="top:3331px">What People Say</h2>
<div class="avatar" style="left:196px;top:3424px" role="img" aria-label="Reviewer portrait"></div>
<p class="t-name" style="left:270px;top:3427px">Helen Marsh</p>
<p class="t-role" style="left:270px;top:3454px">Student</p>
<p class="t-text" style="left:194px;top:3498px">Nell is amazing. She is generous, kind, uncomplicated and candid. We all know dressage is hard, but Nell has a knack for knowing what is.</p>
<p class="stars" style="left:194px;top:3626px">★★★★☆</p>
<div class="avatar" style="left:478px;top:3424px" role="img" aria-label="Reviewer portrait"></div>
<p class="t-name" style="left:552px;top:3427px">Diane Porter</p>
<p class="t-role" style="left:552px;top:3454px">Student</p>
<p class="t-text" style="left:476px;top:3498px">I began riding with Nell this past Spring 2019, and I am thrilled with how much I am learning! Nell's lessons are positive and easy to follow from young.</p>
<p class="stars" style="left:476px;top:3626px">★★★★☆</p>
<div class="avatar" style="left:770px;top:3424px" role="img" aria-label="Reviewer portrait"></div>
<p class="t-name" style="left:844px;top:3427px">Ruth Calloway</p>
<p class="t-role" style="left:844px;top:3454px">Student</p>
<p class="t-text" style="left:768px;top:3498px">Nell comes up for clinics and our students learn so much from her. Her private lessons are very informative and she prioritizes what needs.</p>
<p class="stars" style="left:768px;top:3626px">★★★★☆</p>
<svg class="abs" style="left:558px;top:3690px" width="22" height="22" viewBox="0 0 22 22"><circle cx="11" cy="11" r="9" fill="none" stroke="#c49a6c" stroke-width="1.2"/><circle cx="11" cy="11" r="4" fill="#c49a6c"/></svg>
<span class="dot" style="left:596px;top:3698px"></span>
<span class="dot" style="left:617px;top:3698px"></span>
<span class="dot" style="left:638px;top:3698px"></span>

<!-- Partnerships -->
<section class="partners" role="img" aria-label="Dark background photo of a rider and horse"></section>
<p class="eyebrow" style="top:3842px;color:var(--white)">Trusted By</p>
<h2 class="section-title" style="top:3882px;color:var(--white)">Our Partnerships</h2>
<div class="p-mark" style="left:234px;top:4008px"><span class="shape"></span>Hartwell</div>
<div class="p-mark" style="left:663px;top:4000px"><span class="shape" style="background:#e8e8e8"></span>Brookfield</div>
<h3 class="p-name" style="left:234px;top:4084px">Hartwell Saddlery</h3>
<h3 class="p-name" style="left:662px;top:4084px">Brookfield Saddlery</h3>
<p class="p-text" style="left:232px;top:4142px">Hartwell Saddlery is constantly designing and researching saddles and riders to find the right blend.</p>
<p class="p-text" style="left:660px;top:4142px">My goal is to provide the best possible fit for both horse and rider whether it is a saddle you already own.</p>
<div class="btn btn-ghost" style="left:232px;top:4237px;width:115px;height:38px;font-size:11px;font-weight:500">Read More</div>
<div class="btn btn-ghost" style="left:660px;top:4237px;width:115px;height:38px;font-size:11px;font-weight:500">Know More</div>

<!-- CTA and footer -->
<footer class="footer"></footer>
<h2 class="cta-title">If You are Interested In Learning<br>Training or Lessons, Please Contact Us</h2>
<div class="btn btn-accent" style="left:871px;top:4421px;width:141px;height:61px;border-radius:31px;font-size:14px">Call Now!</div>
<div class="abs" style="left:183px;top:4530px;width:834px;height:1px;background:var(--line)"></div>

<div class="abs" style="left:185px;top:4582px;font-size:20px;font-weight:600;color:var(--ink)">Linden Ridge</div>
<p class="f-text" style="left:189px;top:4643px;width:260px">Lorem ipsum dolor sit amet, consectetur adipisicing elit, sed do eiusmod.</p>
<span class="social" style="left:190px;top:4709px" aria-label="Social link"></span>
<span class="social" style="left:222px;top:4709px" aria-label="Social link"></span>
<span class="social" style="left:256px;top:4709px" aria-label="Social link"></span>
<span class="social" style="left:290px;top:4709px" aria-label="Social link"></span>

<p class="f-head" style="left:543px;top:4580px">Quick Links</p>
<ul class="f-list" style="left:543px;top:4624px"><li>Home</li><li>Services</li><li>News Room</li><li>Blog</li></ul>
<p class="f-head" style="left:700px;top:4580px">Help</p>
<ul class="f-list" style="left:700px;top:4624px"><li>About us</li><li>Login</li><li>Contact Us</li><li>Privacy policy</li><li>Terms&nbsp; conditions</li></ul>
<p class="f-head" style="left:868px;top:4578px">Contact Us</p>
<p class="f-text" style="left:869px;top:4624px;width:150px">Lorem ipsum dolor sit amet consecte.</p>
<svg class="abs" style="left:869px;top:4684px" width="13" height="13" viewBox="0 0 24 24"><path d="M6.6 10.8a15 15 0 0 0 6.6 6.6l2.2-2.2a1 1 0 0 1 1-.25 11.4 11.4 0 0 0 3.6.57 1 1 0 0 1 1 1V20a1 1 0 0 1-1 1A17 17 0 0 1 3 4a1 1 0 0 1 1-1h3.5a1 1 0 0 1 1 1c0 1.25.2 2.45.57 3.57a1 1 0 0 1-.25 1z" fill="#222"/></svg>
<p class="f-text" style="left:900px;top:4681px">555-018-2240</p>
<svg class="abs" style="left:869px;top:4719px" width="13" height="11" viewBox="0 0 26 20"><rect x="1" y="1" width="24" height="18" rx="2" fill="#222"/><path d="M2 3l11 8 11-8" fill="none" stroke="#f3f3f3" stroke-width="2"/></svg>
<p class="f-text" style="left:900px;top:4715px">hello@lindenridge.com</p>
<p class="copyright">Copyright © 2021&nbsp; Linden Ridge All rights reserved</p>

</body>
</html>
```